Clean Energy Brand - Business Card and Letterhead Designs

Hi, everyone! We need a graphic designer who has experience working with the energy sector. We want help designing a perfect two-sided business card and letterhead for a clean energy company we've been assisting. We have a great new logo and all of the associated files.Our client is looking for a design that is "disruptive," "future-facing," "masculine," "bold," and "empowering." The colours of the logo are navy blue and orange and are meant to stand out. We'll need all ownership and copyright paperwork as well as first proofs in a 48-hour period.

Target Market(s)

Government; Non-Profits; Clean Energy Industry; Municipalities; North American Energy Sector

Industry/Entity Type

Power Generation

Requirements
Must have
• A matching business card and letterhead design
Should not have
• Must not be from a template

```html
<!DOCTYPE html>
<html lang="en">
<head>
<meta charset="utf-8">
<title>Northwind Clean Energy — Letterhead</title>
<link href="https://fonts.googleapis.com/css2?family=Open+Sans:wght@400;600;700&display=swap" rel="stylesheet">
<style>
  :root {
    --navy: #1d2a5c;
    --orange: #f15a22;
    --ink: #2b2b2b;
    --rule: #3a3a3a;
    --paper: #ffffff;
    --backdrop: #e6e6e6;
  }
  * { box-sizing: border-box; margin: 0; padding: 0; }
  html, body {
    width: 1200px; height: 910px; overflow: hidden;
    background: var(--backdrop);
    font-family: "Open Sans", Arial, sans-serif;
    color: var(--ink);
  }
  .letterhead {
    position: absolute; left: 290px; top: 17px;
    width: 620px; height: 876px;
    background: var(--paper);
    box-shadow: 0 2px 10px rgba(0,0,0,.12);
    overflow: hidden;
  }
  .brand {
    position: absolute; left: 150px; top: 66px;
    display: flex; align-items: center; gap: 10px;
  }
  .brand-dot { width: 18px; height: 18px; border-radius: 50%; background: var(--orange); }
  .brand-name { font-size: 22px; font-weight: 600; color: var(--navy); letter-spacing: .2px; }
  .content {
    position: absolute; left: 62px; top: 190px; width: 510px;
    font-size: 12px; line-height: 1.7;
  }
  .date { margin-bottom: 30px; }
  .recipient { margin-bottom: 40px; font-style: normal; }
  .salutation { margin-bottom: 6px; }
  .body-text p { margin-bottom: 22px; }
  .closing { margin-top: 38px; }
  .signature { margin-top: 28px; line-height: 1.35; }
  .signature-name { font-weight: 700; font-size: 13px; }
  .footer {
    position: absolute; left: 62px; right: 62px; bottom: 52px;
    font-size: 12px;
  }
  .footer-address { text-align: right; padding-bottom: 10px; }
  .footer-rule { height: 1px; background: var(--rule); }
  .contact-row {
    display: flex; justify-content: space-between; padding-top: 10px;
  }
  .contact-item { display: flex; align-items: center; gap: 6px; }
  .contact-item svg { width: 11px; height: 11px; fill: none; stroke: var(--orange); stroke-width: 2; }
  .color-band { position: absolute; left: 0; right: 0; bottom: 0; height: 10px; }
</style>
</head>
<body>
  <main class="letterhead">
    <header class="brand">
      <span class="brand-dot"></span>
      <span class="brand-name">Northwind Clean Energy</span>
    </header>

    <section class="content">
      <p class="date">Date: 20 November 2018</p>
      <address class="recipient">
        To<br>
        Maplebrook Garden Ltd.<br>
        48 Orchard Lane, Suite# B<br>
        London, UK 1400B27
      </address>
      <p class="salutation">Dear Carter,</p>
      <div class="body-text">
        <p>Lorem Ipsum is simply dummy text of the printing and typesetting industry. Lorem Ipsum has been the industry's standard dummy text ever since the 1500s, when an unknown printer took a galley of type and scrambled it to make a type specimen book. It has survived not only five centuries, but also the leap into electronic typesetting, remaining essentially unchanged. It was popularised in the 1960s with the release of Drylinea sheets containing Lorem Ipsum passages, and more recently with desktop publishing software like Quillset Layout including versions of Lorem Ipsum.</p>
        <p>Lorem Ipsum is simply dummy text of the printing and typesetting industry. Lorem Ipsum has been the industry's.</p>
      </div>
      <p class="closing">Thanking you</p>
      <div class="signature">
        <p class="signature-name">Daniel Hartley</p>
        <p class="signature-title">CMCA</p>
      </div>
    </section>

    <footer class="footer">
      <p class="footer-address">912 NW Ridge Rd., Suite 6, Zip code is 97810</p>
      <div class="footer-rule"></div>
      <div class="contact-row">
        <span class="contact-item">
          <svg viewBox="0 0 12 12"><path d="M2 1.5h2.5l1 2.5-1.5 1a6 6 0 0 0 3 3l1-1.5 2.5 1V11A9 9 0 0 1 1 2.5z"/></svg>
          555-210-4876
        </span>
        <span class="contact-item">
          <svg viewBox="0 0 12 12"><rect x="1" y="2.5" width="10" height="7"/><path d="M1 2.5l5 4 5-4"/></svg>
          info@northwindenergy.com
        </span>
        <span class="contact-item">
          <svg viewBox="0 0 12 12"><circle cx="6" cy="6" r="5"/><path d="M1 6h10M6 1c-3 3-3 7 0 10M6 1c3 3 3 7 0 10"/></svg>
          www.northwindenergy.com
        </span>
      </div>
    </footer>

    <svg class="color-band" viewBox="0 0 620 10" preserveAspectRatio="none" aria-hidden="true">
      <polygon points="0,0 296,0 290,10 0,10" fill="var(--orange)"/>
      <polygon points="302,0 620,0 620,10 296,10" fill="var(--navy)"/>
    </svg>
  </main>
</body>
</html>
```